ready mix concrete business

i need a logo for a ready mix company
it is called Pine Hollow Concrete for business cards and promotional items. would like a ready mix truck on it
and must look profesional

```html
<!DOCTYPE html>
<html lang="en">
<head>
<meta charset="utf-8">
<title>Pine Hollow Concrete – Business Card</title>
<link rel="stylesheet" href="https://fonts.googleapis.com/css2?family=Noto+Sans:wght@400;700&display=swap">
<style>
  :root {
    --stage-bg: #1c1c1c;
    --card-bg: #d5d5d3;
    --ink: #2b2d2e;
    --ink-soft: #333536;
    --rule: #2e3031;
  }
  * { box-sizing: border-box; margin: 0; padding: 0; }
  html, body {
    width: 1200px;
    height: 902px;
    overflow: hidden;
    background: var(--stage-bg);
  }
  .stage {
    position: relative;
    width: 1200px;
    height: 902px;
  }
  .business-card {
    position: absolute;
    left: 130px;
    top: 184px;
    width: 940px;
    height: 534px;
    background: var(--card-bg);
    font-family: "Noto Sans", Arial, sans-serif;
    color: var(--ink);
  }
  .brand {
    position: absolute;
    left: 0;
    right: 0;
    top: 70px;
    text-align: center;
  }
  .brand-mark {
    display: block;
    width: 64px;
    height: 64px;
    margin: 0 auto 26px;
    background: var(--ink);
  }
  .brand-name {
    font-weight: 700;
    font-size: 52px;
    line-height: 1;
    letter-spacing: 2px;
    color: var(--ink);
  }
  .brand-tagline {
    display: flex;
    align-items: center;
    justify-content: center;
    gap: 14px;
    margin-top: 12px;
  }
  .brand-tagline .rule {
    width: 88px;
    height: 2px;
    background: var(--rule);
  }
  .brand-tagline .word {
    font-weight: 700;
    font-size: 28px;
    letter-spacing: 5px;
    color: var(--ink);
  }
  .contact-person {
    position: absolute;
    left: 0;
    right: 0;
    top: 334px;
    display: flex;
    align-items: center;
  }
  .contact-person .rule {
    flex: 1;
    height: 2px;
    background: var(--rule);
  }
  .person-name {
    padding: 0 10px;
    font-weight: 700;
    font-size: 29px;
    letter-spacing: 0.5px;
    line-height: 1.2;
    color: var(--ink);
  }
  .person-role {
    position: absolute;
    left: 0;
    right: 0;
    top: 370px;
    text-align: center;
    font-size: 22px;
    color: var(--ink-soft);
  }
  .contact-details {
    position: absolute;
    left: 0;
    right: 0;
    top: 424px;
    text-align: center;
    font-size: 24px;
    line-height: 36px;
    color: var(--ink-soft);
  }
</style>
</head>
<body>
  <main class="stage">
    <section class="business-card">
      <div class="brand">
        <span class="brand-mark" aria-hidden="true"></span>
        <h1 class="brand-name">PINE HOLLOW</h1>
        <div class="brand-tagline">
          <span class="rule"></span>
          <span class="word">CONCRETE</span>
          <span class="rule"></span>
        </div>
      </div>

      <div class="contact-person">
        <span class="rule"></span>
        <h2 class="person-name">EMPLOYEE NAME</h2>
        <span class="rule"></span>
      </div>
      <p class="person-role">Director</p>

      <div class="contact-details">
        <p class="phone">000-000-0000</p>
        <p class="email">office@pinehollowconcrete.com</p>
      </div>
    </section>
  </main>
</body>
</html>
```